Redesign Of Current Landing Page

I need to redesign this landing page https://www.bluewillowpromos.example/?page=landing&landing=23 (Please do not opt in because when you do it will show you the home page. Please clear your cookies before going to this url above to view the 1 page landing page.)

Please use my updated website as a reference for colors and logo.
http://sitecraftorly.example/dh/bwpg/index.html

I would like the call to action to be a button that opens into a lead form...

Button would be "Download Samples"

Target Market(s)

small business owners

Industry/Entity Type

Marketing

Number of Pages Required

1 page

Colors

Designer to choose colors to be used in the design.

Requirements
Must have
• must be full responsive on all devices
Nice to have
• must have a legitimate professional apeal to it
Should not have
• open

```html
<!DOCTYPE html>
<html lang="en">
<head>
<meta charset="utf-8">
<title>Blue Willow Promos – Attract More Customers</title>
<link href="https://fonts.googleapis.com/css2?family=Raleway:wght@500;600;700&family=Roboto:wght@300;400;500;700&display=swap" rel="stylesheet">
<style>
:root{
  --navy:#0f2a47;
  --navy-deep:#0a1f36;
  --blue:#1a73c8;
  --blue-bright:#2a8be0;
  --orange:#f9a51a;
  --orange-dark:#e6930b;
  --ink:#2b2b2b;
  --muted:#666a70;
  --line:#e3e3e3;
  --paper:#ffffff;
  --quote-bg:#efefef;
  --footer:#1d1f22;
}
*{box-sizing:border-box;margin:0;padding:0}
html,body{width:1200px;height:2695px;overflow:hidden}
body{font-family:"Roboto",Arial,sans-serif;color:var(--ink);background:var(--paper);position:relative}
.wrap{position:relative;width:1200px}
.abs{position:absolute}

/* buttons */
.cta{position:absolute;display:flex;align-items:center;background:var(--orange);color:#fff;text-decoration:none;
  font-family:"Raleway",sans-serif;font-weight:700;text-transform:uppercase;border-radius:3px;box-shadow:0 3px 0 var(--orange-dark)}
.cta .ico{width:34px;height:34px;border:2px dashed rgba(255,255,255,.85);border-radius:3px;display:flex;align-items:center;justify-content:center;margin:0 34px 0 28px;flex:none}
.cta .label{font-size:18px;line-height:20px}
.cta.big{width:345px;height:72px}

/* hero */
.hero{height:598px;background:radial-gradient(ellipse at 20% 20%,#1f4670 0%,var(--navy) 55%,var(--navy-deep) 100%);color:#fff}
.topbar{top:8px;right:60px;display:flex;gap:34px;font-size:13px;color:#dfe7f0}
.topbar span{display:flex;align-items:center;gap:7px}
.brand{top:48px;left:111px;display:flex;align-items:center;gap:12px}
.brand .mark{width:40px;height:40px;background:var(--blue-bright)}
.brand .name{font-family:"Raleway",sans-serif;font-weight:700;font-size:26px;color:var(--blue-bright);letter-spacing:1px;text-transform:uppercase}
.header-cta{top:50px;right:108px;width:385px;height:40px;font-size:13px;box-shadow:none}
.header-cta .ico{width:22px;height:22px;margin:0 22px 0 12px;border-width:1.5px}
.hero h1{top:232px;left:111px;font-family:"Raleway",sans-serif;font-weight:600;font-size:33px;letter-spacing:.5px}
.hero .rule{top:282px;left:111px;width:430px;height:2px;background:rgba(255,255,255,.8)}
.hero .rule::after{content:"";position:absolute;left:210px;top:0;border:8px solid transparent;border-top-color:rgba(255,255,255,.8)}
.hero .lead{top:312px;left:111px;width:500px;font-size:17px;line-height:23px;text-transform:uppercase;color:#e5ecf4;letter-spacing:.3px}
.hero .cta.big{top:413px;left:111px}
.hero-art{left:600px;top:210px;width:560px;height:388px;overflow:hidden}
.hero-art .disc{position:absolute;left:0;top:20px;width:560px;height:560px;border-radius:50%;background:var(--blue)}
.hero-art .stack{position:absolute;left:70px;top:10px;width:400px;height:330px;border-radius:6px;
  background:linear-gradient(135deg,#c43c3c 0%,#e28b3a 30%,#2e6aa8 60%,#26303d 100%)}

/* incentives */
.incentives{top:598px;height:587px;width:1200px;text-align:center}
.incentives h2{position:absolute;top:47px;width:1200px;font-family:"Raleway",sans-serif;font-weight:600;font-size:23px;color:#333}
.card{position:absolute;top:112px;width:225px}
.card h3{font-size:15px;font-weight:500;line-height:18px;height:40px;color:#222}
.card .photo{height:152px;margin-bottom:16px}
.card p{font-size:13px;line-height:20px;color:var(--muted);padding:0 12px}
.card strong{color:var(--blue);font-size:17px;font-weight:500}
.incentives .cta.big{top:462px;left:427px}

/* imagine */
.imagine{top:1185px;height:489px;width:1200px;border-top:1px solid var(--line);border-bottom:1px solid var(--line)}
.col{position:absolute;top:48px;width:470px}
.col h2{font-family:"Raleway",sans-serif;font-weight:600;font-size:21px;color:#333;margin-bottom:22px}
.col p{font-size:13px;line-height:21px;color:var(--muted);margin-bottom:20px}
.divider{position:absolute;left:600px;top:48px;width:1px;height:210px;background:var(--line)}
.imagine .cta.big{top:363px;left:427px}

/* why */
.why{top:1674px;height:469px;width:1200px;background:linear-gradient(180deg,#2c3646 0%,#1e2835 100%);text-align:center}
.why h2{position:absolute;top:50px;width:1200px;font-family:"Raleway",sans-serif;font-weight:600;font-size:22px;color:#fff}
.reason{position:absolute;top:102px;width:149px;height:191px;background:#fff;border-radius:2px;overflow:hidden}
.reason .top{height:111px;background:var(--blue);display:flex;align-items:center;justify-content:center;position:relative}
.reason .top::after{content:"";position:absolute;bottom:-1px;left:0;width:0;height:0;border-left:149px solid #fff;border-top:14px solid transparent}
.reason p{font-size:12px;line-height:18px;color:#555;padding:10px 10px 0}
.why .cta.big{top:346px;left:427px}

/* testimonial */
.testimonial{top:2143px;height:407px;width:1200px}
.testimonial h2{position:absolute;top:50px;left:111px;font-family:"Raleway",sans-serif;font-weight:600;font-size:21px;color:#333}
.quote{position:absolute;top:102px;left:111px;width:643px;height:207px;background:var(--quote-bg);padding:30px 34px 0 92px;font-size:13px;line-height:21px;color:#555}
.quote .qmark{position:absolute;left:30px;top:34px}
.quote::after{content:"";position:absolute;left:96px;bottom:-24px;border-left:24px solid var(--quote-bg);border-bottom:24px solid transparent}
.who{position:absolute;top:2471px;left:240px;font-size:14px;line-height:22px;color:#555}
.who b{color:var(--blue);font-weight:500}
.portrait{position:absolute;top:2178px;left:736px;width:395px;height:372px;background:linear-gradient(180deg,#f4f5f6 0%,#dfe2e6 100%)}

/* footer */
.footer{top:2550px;height:145px;width:1200px;background:var(--footer)}
.footer .fname{position:absolute;top:36px;left:111px;font-family:"Raleway",sans-serif;font-weight:700;font-size:21px;color:#8b8f95;text-transform:uppercase;letter-spacing:1px}
.footer small{position:absolute;top:80px;left:111px;font-size:12px;line-height:20px;color:#8b8f95}
.footer .cta.big{top:36px;left:742px}
</style>
</head>
<body>
<div class="wrap">

  <header class="hero abs" style="top:0;left:0;width:1200px">
    <div class="topbar abs">
      <span><svg width="10" height="14" viewBox="0 0 10 14"><rect x="1" y="0" width="8" height="14" rx="1.5" fill="#4aa3f0"/><rect x="2.5" y="2" width="5" height="8" fill="#0f2a47"/></svg>1-800-555-0142</span>
      <span><svg width="13" height="13" viewBox="0 0 13 13"><circle cx="6.5" cy="6.5" r="5.5" fill="none" stroke="#4aa3f0" stroke-width="1.6"/><path d="M6.5 3.5v3.2l2 1.3" stroke="#4aa3f0" stroke-width="1.4" fill="none"/></svg>Mon-Fri : 8am-5pm PST</span>
    </div>
    <div class="brand abs"><span class="mark"></span><span class="name">Blue Willow Promos</span></div>
    <a class="cta header-cta" href="#samples"><span class="ico"><svg width="10" height="12" viewBox="0 0 10 12"><path d="M5 1v8M1.5 6l3.5 3.5L8.5 6" stroke="#fff" stroke-width="1.6" fill="none"/></svg></span><span class="label" style="font-size:13px">Download Free Samples of Our Incentives</span></a>

    <h1 class="abs">ATTRACT MORE CUSTOMERS</h1>
    <div class="rule abs"></div>
    <p class="lead abs">Who spend more money with your business more often using free vacation &amp; cruise certificates and other incentives without breaking the bank!</p>
    <a class="cta big" href="#samples"><span class="ico"><svg width="14" height="16" viewBox="0 0 14 16"><path d="M7 1v11M2 7.5l5 5 5-5" stroke="#fff" stroke-width="2" fill="none"/></svg></span><span class="label">Download Free Samples<br>of Our Incentives</span></a>

    <div class="hero-art abs">
      <div class="disc"></div>
      <div class="stack" role="img" aria-label="Fanned stack of printed incentive certificates for cruises, cash back, gadgets and vacations"></div>
    </div>
  </header>

  <section class="incentives abs">
    <h2>FOR $99/MTH YOU CAN GIVEAWAY AN UNLIMITED AMOUNT OF ALL OUR INCENTIVES</h2>
    <div class="card" style="left:111px">
      <h3>Vacation Getaway<br>Certificates</h3>
      <div class="photo" role="img" aria-label="Person booking a vacation on a laptop" style="background:linear-gradient(135deg,#8d8f93,#d8dadd 60%,#5f6165)"></div>
      <p>7 Night Hotel Stays, Cruises &amp; Airfares Up To <strong>$3000.00</strong> Retail Value Your Customers Just Pay Taxes!</p>
    </div>
    <div class="card" style="left:361px">
      <h3>Restaurant Gift<br>Certificates</h3>
      <div class="photo" role="img" aria-label="Chef plating a restaurant dish" style="background:linear-gradient(135deg,#e7e5e2,#b9b3ab 50%,#5a4a3c)"></div>
      <p><strong>$25-$300</strong> Retail Value Thousands Of Restaurants Nationwide!</p>
    </div>
    <div class="card" style="left:612px">
      <h3>Electronic Product<br>Giveaways</h3>
      <div class="photo" role="img" aria-label="Assorted tablets, phones, earbuds and gadgets" style="background:linear-gradient(135deg,#3d8fd6,#9fc9ec 50%,#2c4f78)"></div>
      <p>Tablets, Premium Earbuds, Smart Watches, Mp4 Players <strong>$100-$150</strong> Retail Value</p>
    </div>
    <div class="card" style="left:862px">
      <h3>Gas Or Grocery<br>Rewards</h3>
      <div class="photo" role="img" aria-label="Hand holding a fuel pump nozzle" style="background:linear-gradient(135deg,#3a4350,#8a94a2 50%,#1f4f8f)"></div>
      <p>Available In <strong>$50-$100</strong> Denominations</p>
    </div>
    <a class="cta big" href="#samples"><span class="ico"><svg width="14" height="16" viewBox="0 0 14 16"><path d="M7 1v11M2 7.5l5 5 5-5" stroke="#fff" stroke-width="2" fill="none"/></svg></span><span class="label">Download Free Samples<br>of Our Incentives</span></a>
  </section>

  <section class="imagine abs">
    <div class="col" style="left:111px">
      <h2>IMAGINE</h2>
      <p>Being able to create exciting give away promotions that will boost your sales without ever having to worry about cost.</p>
      <p>Blue Willow Promo Group, Inc. provides high-perceived value promotional incentives to businesses that want to advertise an exciting Give Away that will instantly attract more customers from your existing advertising efforts.</p>
      <p>Your business can give away incentive certificates that are redeemable for luxury hotel &amp; resort stays with airfare included, cruises, cash for gas, groceries, dining and even electronic goods.</p>
    </div>
    <div class="divider"></div>
    <div class="col" style="left:625px">
      <h2>HOW CAN WE DO IT?</h2>
      <p>Being able to create exciting give away promotions that will boost your sales without ever having to worry about cost.</p>
      <p>Blue Willow Promo Group, Inc. provides high-perceived value promotional incentives to businesses that want to advertise an exciting Give Away that will instantly attract more customers from your existing advertising efforts.</p>
      <p>Your business can give away incentive certificates that are redeemable for luxury hotel &amp; resort stays with airfare included, cruises, cash for gas, groceries, dining and even electronic goods.</p>
    </div>
    <a class="cta big" href="#samples"><span class="ico"><svg width="14" height="16" viewBox="0 0 14 16"><path d="M7 1v11M2 7.5l5 5 5-5" stroke="#fff" stroke-width="2" fill="none"/></svg></span><span class="label">Download Free Samples<br>of Our Incentives</span></a>
  </section>

  <section class="why abs">
    <h2>WHY OFFER INCENTIVES TO CUSTOMERS?</h2>
    <div class="reason" style="left:111px"><div class="top"><svg width="52" height="44" viewBox="0 0 52 44" fill="#fff"><rect x="4" y="30" width="7" height="12"/><rect x="15" y="24" width="7" height="18"/><rect x="26" y="17" width="7" height="25"/><rect x="37" y="9" width="7" height="33"/><path d="M3 24L22 8l8 6L46 2" stroke="#fff" stroke-width="2.5" fill="none"/></svg></div><p>Increase Responses From Your Existing Ads</p></div>
    <div class="reason" style="left:276px"><div class="top"><svg width="44" height="44" viewBox="0 0 44 44"><path d="M6 38L24 20" stroke="#fff" stroke-width="7" stroke-linecap="round"/><circle cx="30" cy="14" r="10" fill="#fff"/><rect x="30" y="2" width="9" height="9" fill="#1a73c8" transform="rotate(45 34 7)"/></svg></div><p>#1 Sales Closing Tool - Gift w/ Purchase</p></div>
    <div class="reason" style="left:441px"><div class="top"><svg width="46" height="44" viewBox="0 0 46 44"><path d="M23 2l6.2 13.6 14.8 1.6-11 10 3.1 14.6L23 34.3 9.9 41.8 13 27.2 2 17.2l14.8-1.6z" fill="#fff"/></svg></div><p>Build Brand Awareness and Trust</p></div>
    <div class="reason" style="left:606px"><div class="top"><svg width="50" height="44" viewBox="0 0 50 44" fill="#fff"><circle cx="32" cy="12" r="8"/><path d="M18 40c0-10 6-16 14-16s14 6 14 16z"/><circle cx="18" cy="15" r="7" stroke="#1a73c8" stroke-width="2"/><path d="M4 42c0-10 6-15 14-15s14 5 14 15z" stroke="#1a73c8" stroke-width="2"/></svg></div><p>Insure The Sale Over Your Competition</p></div>
    <div class="reason" style="left:771px"><div class="top"><svg width="48" height="40" viewBox="0 0 48 40" fill="none" stroke="#fff" stroke-width="4"><path d="M4 12h36M32 4l8 8-8 8"/><path d="M44 28H8M16 20l-8 8 8 8"/></svg></div><p>Boost Repeat and Referral Business</p></div>
    <div class="reason" style="left:936px"><div class="top"><svg width="46" height="46" viewBox="0 0 46 46"><circle cx="23" cy="23" r="20" fill="none" stroke="#fff" stroke-width="3"/><circle cx="23" cy="23" r="14" fill="#fff"/><text x="23" y="31" text-anchor="middle" font-family="Roboto,sans-serif" font-weight="700" font-size="22" fill="#1a73c8">$</text></svg></div><p>Improve Retention Rates</p></div>
    <a class="cta big" href="#samples"><span class="ico"><svg width="14" height="16" viewBox="0 0 14 16"><path d="M7 1v11M2 7.5l5 5 5-5" stroke="#fff" stroke-width="2" fill="none"/></svg></span><span class="label">Download Free Samples<br>of Our Incentives</span></a>
  </section>

  <section class="testimonial abs">
    <h2>WHAT ABOUT OUR CLIENT SAYS</h2>
    <div class="quote">
      <svg class="qmark" width="38" height="30" viewBox="0 0 38 30" fill="#1a73c8"><path d="M0 16C0 6 6 1 14 0v5c-4 1-7 4-7 8h7v17H0zM21 16c0-10 6-15 14-16v5c-4 1-7 4-7 8h7v17H21z"/></svg>
      I began using your incentives two years ago to boost lead generation efforts. I have experienced a 63% increase in lead captures. And, even more importantly, my sales have increased as well. The ability to offer unlimited certificates and not having to pay for each certificate I give away is perhaps the best feature of the program, but having the flexibility to email or print certificates for my customers is also wonderful. I even use your html banners to automate my promotions right on my website!,
    </div>
  </section>
  <div class="who"><b>Dan R.</b><br>Oakfield, TN</div>
  <div class="portrait" role="img" aria-label="Smiling businessman in a grey suit with arms crossed"></div>

  <footer class="footer abs">
    <div class="fname">Blue Willow Promos</div>
    <small>© 2017 Blue Willow Promo Group, Inc. All Rights Reserved<br>Terms of Use &nbsp;|&nbsp; Privacy Policy</small>
    <a class="cta big" href="#samples"><span class="ico"><svg width="14" height="16" viewBox="0 0 14 16"><path d="M7 1v11M2 7.5l5 5 5-5" stroke="#fff" stroke-width="2" fill="none"/></svg></span><span class="label">Download Free Samples<br>of Our Incentives</span></a>
  </footer>

</div>
</body>
</html>
```